Business Card Design Project

Double-side business card.
Side One:
Logo (Including the word TOLVEKA that is part of the Logo
"Programas de Renovación Urbana y Cuidado del Entorno Natural Andino"
Side Two:
Marcela Ostrander
Co-Founder & CEO
Boulder, CO (USA)
email: marcelao@tolveka.example (please use an icon for "emal")
cell: +1 (202) 555 0147 (please use an icon for "cell")
skype: marceostrander (please use an icon for "skype")
twitter: marceostrander (please use an icon for "twitter")
www.tolveka.example
Target Market(s)
Foundations, Governments, and Private sector companies that implement projects for sustainability.
Industry/Entity Type
Business
Font styles to use
Colors
Designer to choose colors to be used in the design.
Requirements
Nice to have
- barcode

```html
<!DOCTYPE html>
<html lang="es">
<head>
<meta charset="utf-8">
<title>TOLVEKA – Tarjetas de presentación</title>
<link rel="stylesheet" href="https://fonts.googleapis.com/css2?family=Source+Sans+3:wght@400;600&display=swap">
<style>
  :root {
    --sky: #4fc3f4;
    --leaf: #52c383;
    --coral: #f26366;
    --plum: #a97daa;
    --ink-grey: #6f6f73;
    --frame: #2b2b2b;
    --paper: #ffffff;
    --card-w: 418px;
    --card-h: 237px;
  }
  * { box-sizing: border-box; margin: 0; padding: 0; }
  html, body {
    width: 1034px;
    height: 1200px;
    overflow: hidden;
    background: var(--paper);
    font-family: "Source Sans 3", "Myriad Pro", Arial, sans-serif;
  }
  .sheet { position: relative; width: 1034px; height: 1200px; }

  .card {
    position: absolute;
    width: var(--card-w);
    height: var(--card-h);
    border: 1px solid var(--frame);
    background: var(--paper);
    overflow: hidden;
  }
  .card--sky   { --accent: var(--sky); }
  .card--leaf  { --accent: var(--leaf); }
  .card--coral { --accent: var(--coral); }
  .card--plum  { --accent: var(--plum); }

  /* Front side */
  .front__brand {
    position: absolute;
    left: 0; right: 0; top: 60px;
    display: flex;
    align-items: center;
    justify-content: center;
    gap: 16px;
  }
  .front__mark {
    width: 34px; height: 34px;
    background: var(--accent);
  }
  .front__name {
    font-size: 50px;
    font-weight: 400;
    letter-spacing: 3px;
    color: var(--ink-grey);
    line-height: 1;
  }
  .front__band {
    position: absolute;
    left: 0; right: 0; bottom: 0;
    height: 42px;
    background: var(--accent);
    display: flex;
    align-items: center;
    padding-left: 8px;
  }
  .front__tagline {
    color: var(--paper);
    font-size: 11.4px;
    white-space: nowrap;
  }

  /* Back side */
  .back__panel {
    position: absolute;
    left: 0; top: 0; bottom: 0;
    width: 210px;
    background: var(--accent);
  }
  .back__identity {
    position: absolute;
    right: calc(var(--card-w) - 206px);
    top: 20px;
    text-align: right;
    color: var(--paper);
    font-size: 16.5px;
    line-height: 22px;
  }
  .back__contacts {
    position: absolute;
    left: 183px;
    top: 97px;
    list-style: none;
  }
  .contact {
    display: flex;
    align-items: center;
    height: 22px;
  }
  .contact__icon {
    width: 18px; height: 18px;
    margin-right: 13px;
    flex: none;
  }
  .contact__text {
    color: var(--ink-grey);
    font-size: 16px;
    white-space: nowrap;
  }
</style>
</head>
<body>
<main class="sheet">

  <!-- Row 1: sky -->
  <section class="card card--sky" style="left:50px; top:41px;">
    <div class="front__brand"><span class="front__mark"></span><span class="front__name">TOLVEKA</span></div>
    <div class="front__band"><p class="front__tagline">Programas de Renovación Urbana y Cuidado del Entorno Natural Andino</p></div>
  </section>
  <section class="card card--sky" style="left:568px; top:41px;">
    <div class="back__panel"></div>
    <div class="back__identity"><p>Marcela Ostrander</p><p>Co-Founder &amp; CEO</p><p>Boulder, CO (USA)</p></div>
    <ul class="back__contacts">
      <li class="contact"><svg class="contact__icon" viewBox="0 0 18 18"><rect x="2" y="4" width="14" height="10" fill="#fff"/><path d="M2 4 L9 10 L16 4" fill="none" stroke="var(--accent)" stroke-width="1.4"/></svg><span class="contact__text">marcelao@tolveka.example</span></li>
      <li class="contact"><svg class="contact__icon" viewBox="0 0 18 18"><path d="M5 2 L8 6 L6.5 8 C7.5 10 8.5 11 10.5 12 L12.5 10.5 L16 13.5 L14 16 C8 15.5 2.5 10 2.5 4 Z" fill="#fff"/></svg><span class="contact__text">+1 (202) 555 0147</span></li>
      <li class="contact"><svg class="contact__icon" viewBox="0 0 18 18"><circle cx="9" cy="9" r="7" fill="#fff"/></svg><span class="contact__text">marceostrander</span></li>
      <li class="contact"><svg class="contact__icon" viewBox="0 0 18 18"><circle cx="9" cy="9" r="7" fill="#fff"/></svg><span class="contact__text">marceostrander</span></li>
      <li class="contact"><svg class="contact__icon" viewBox="0 0 18 18"><circle cx="9" cy="9" r="7" fill="#fff"/><g fill="none" stroke="var(--accent)" stroke-width="1.1"><ellipse cx="9" cy="9" rx="3" ry="6"/><line x1="3" y1="9" x2="15" y2="9"/><path d="M4 6 H14 M4 12 H14"/></g></svg><span class="contact__text">tolveka.example</span></li>
    </ul>
  </section>

  <!-- Row 2: leaf -->
  <section class="card card--leaf" style="left:50px; top:328px;">
    <div class="front__brand"><span class="front__mark"></span><span class="front__name">TOLVEKA</span></div>
    <div class="front__band"><p class="front__tagline">Programas de Renovación Urbana y Cuidado del Entorno Natural Andino</p></div>
  </section>
  <section class="card card--leaf" style="left:568px; top:328px;">
    <div class="back__panel"></div>
    <div class="back__identity"><p>Marcela Ostrander</p><p>Co-Founder &amp; CEO</p><p>Boulder, CO (USA)</p></div>
    <ul class="back__contacts">
      <li class="contact"><svg class="contact__icon" viewBox="0 0 18 18"><rect x="2" y="4" width="14" height="10" fill="#fff"/><path d="M2 4 L9 10 L16 4" fill="none" stroke="var(--accent)" stroke-width="1.4"/></svg><span class="contact__text">marcelao@tolveka.example</span></li>
      <li class="contact"><svg class="contact__icon" viewBox="0 0 18 18"><path d="M5 2 L8 6 L6.5 8 C7.5 10 8.5 11 10.5 12 L12.5 10.5 L16 13.5 L14 16 C8 15.5 2.5 10 2.5 4 Z" fill="#fff"/></svg><span class="contact__text">+1 (202) 555 0147</span></li>
      <li class="contact"><svg class="contact__icon" viewBox="0 0 18 18"><circle cx="9" cy="9" r="7" fill="#fff"/></svg><span class="contact__text">marceostrander</span></li>
      <li class="contact"><svg class="contact__icon" viewBox="0 0 18 18"><circle cx="9" cy="9" r="7" fill="#fff"/></svg><span class="contact__text">marceostrander</span></li>
      <li class="contact"><svg class="contact__icon" viewBox="0 0 18 18"><circle cx="9" cy="9" r="7" fill="#fff"/><g fill="none" stroke="var(--accent)" stroke-width="1.1"><ellipse cx="9" cy="9" rx="3" ry="6"/><line x1="3" y1="9" x2="15" y2="9"/><path d="M4 6 H14 M4 12 H14"/></g></svg><span class="contact__text">tolveka.example</span></li>
    </ul>
  </section>

  <!-- Row 3: coral -->
  <section class="card card--coral" style="left:50px; top:641px;">
    <div class="front__brand"><span class="front__mark"></span><span class="front__name">TOLVEKA</span></div>
    <div class="front__band"><p class="front__tagline">Programas de Renovación Urbana y Cuidado del Entorno Natural Andino</p></div>
  </section>
  <section class="card card--coral" style="left:568px; top:641px;">
    <div class="back__panel"></div>
    <div class="back__identity"><p>Marcela Ostrander</p><p>Co-Founder &amp; CEO</p><p>Boulder, CO (USA)</p></div>
    <ul class="back__contacts">
      <li class="contact"><svg class="contact__icon" viewBox="0 0 18 18"><rect x="2" y="4" width="14" height="10" fill="#fff"/><path d="M2 4 L9 10 L16 4" fill="none" stroke="var(--accent)" stroke-width="1.4"/></svg><span class="contact__text">marcelao@tolveka.example</span></li>
      <li class="contact"><svg class="contact__icon" viewBox="0 0 18 18"><path d="M5 2 L8 6 L6.5 8 C7.5 10 8.5 11 10.5 12 L12.5 10.5 L16 13.5 L14 16 C8 15.5 2.5 10 2.5 4 Z" fill="#fff"/></svg><span class="contact__text">+1 (202) 555 0147</span></li>
      <li class="contact"><svg class="contact__icon" viewBox="0 0 18 18"><circle cx="9" cy="9" r="7" fill="#fff"/></svg><span class="contact__text">marceostrander</span></li>
      <li class="contact"><svg class="contact__icon" viewBox="0 0 18 18"><circle cx="9" cy="9" r="7" fill="#fff"/></svg><span class="contact__text">marceostrander</span></li>
      <li class="contact"><svg class="contact__icon" viewBox="0 0 18 18"><circle cx="9" cy="9" r="7" fill="#fff"/><g fill="none" stroke="var(--accent)" stroke-width="1.1"><ellipse cx="9" cy="9" rx="3" ry="6"/><line x1="3" y1="9" x2="15" y2="9"/><path d="M4 6 H14 M4 12 H14"/></g></svg><span class="contact__text">tolveka.example</span></li>
    </ul>
  </section>

  <!-- Row 4: plum -->
  <section class="card card--plum" style="left:55px; top:918px;">
    <div class="front__brand"><span class="front__mark"></span><span class="front__name">TOLVEKA</span></div>
    <div class="front__band"><p class="front__tagline">Programas de Renovación Urbana y Cuidado del Entorno Natural Andino</p></div>
  </section>
  <section class="card card--plum" style="left:573px; top:918px;">
    <div class="back__panel"></div>
    <div class="back__identity"><p>Marcela Ostrander</p><p>Co-Founder &amp; CEO</p><p>Boulder, CO (USA)</p></div>
    <ul class="back__contacts">
      <li class="contact"><svg class="contact__icon" viewBox="0 0 18 18"><rect x="2" y="4" width="14" height="10" fill="#fff"/><path d="M2 4 L9 10 L16 4" fill="none" stroke="var(--accent)" stroke-width="1.4"/></svg><span class="contact__text">marcelao@tolveka.example</span></li>
      <li class="contact"><svg class="contact__icon" viewBox="0 0 18 18"><path d="M5 2 L8 6 L6.5 8 C7.5 10 8.5 11 10.5 12 L12.5 10.5 L16 13.5 L14 16 C8 15.5 2.5 10 2.5 4 Z" fill="#fff"/></svg><span class="contact__text">+1 (202) 555 0147</span></li>
      <li class="contact"><svg class="contact__icon" viewBox="0 0 18 18"><circle cx="9" cy="9" r="7" fill="#fff"/></svg><span class="contact__text">marceostrander</span></li>
      <li class="contact"><svg class="contact__icon" viewBox="0 0 18 18"><circle cx="9" cy="9" r="7" fill="#fff"/></svg><span class="contact__text">marceostrander</span></li>
      <li class="contact"><svg class="contact__icon" viewBox="0 0 18 18"><circle cx="9" cy="9" r="7" fill="#fff"/><g fill="none" stroke="var(--accent)" stroke-width="1.1"><ellipse cx="9" cy="9" rx="3" ry="6"/><line x1="3" y1="9" x2="15" y2="9"/><path d="M4 6 H14 M4 12 H14"/></g></svg><span class="contact__text">tolveka.example</span></li>
    </ul>
  </section>

</main>
</body>
</html>
```